Business Card/Letterhead/Envelope design
KTL & Associates
Business Card/Letterhead/Envelope design -
Creative Brief
Professional
Gregory P. Holt
Principal
2947 Brambleton Way Suite 340 Frisco, Texas 75981
gregory@ktlva.com
www.ktlva.com
Rounded corners preferable Simple Clean Cutting Edge Front: Full Color on White background or Full Color on Black background Back: Full Color on Black background
Reversed Logo centered on the back of card w/slogan of company... Passion. Performance. Results. (Black background)

```html
<!DOCTYPE html>
<html lang="en">
<head>
<meta charset="utf-8">
<title>KTL &amp; Associates – Stationery Set</title>
<link href="https://fonts.googleapis.com/css2?family=Montserrat:wght@400;600;700&display=swap" rel="stylesheet">
<style>
  :root{
    --bg:#bdbdbd;
    --paper:#ffffff;
    --red:#c8151b;
    --red-dark:#8e0c10;
    --ink:#2b2b2b;
    --grey:#7a7a7a;
    --grey-light:#e3e3e3;
    --black:#111111;
  }
  *{box-sizing:border-box;margin:0;padding:0}
  html,body{width:1200px;height:312px;overflow:hidden;background:var(--bg);font-family:"Montserrat",Arial,sans-serif;color:var(--ink)}
  .canvas{position:relative;width:1200px;height:312px}
  .piece{position:absolute;background:var(--paper);box-shadow:0 1px 3px rgba(0,0,0,.35);overflow:hidden}
  .piece svg.trim{position:absolute;inset:0;width:100%;height:100%}

  /* business cards */
  .card{width:79px;height:43px;border-radius:3px}
  .card--dark{background:var(--black)}
  .card .brand{position:absolute;left:5px;top:7px;font-size:6px;font-weight:700;color:var(--red);line-height:1}
  .card--dark .brand{left:0;right:0;top:14px;text-align:center;font-size:7px}
  .card .slogan{position:absolute;left:0;right:0;top:25px;text-align:center;font-size:3px;color:var(--grey-light)}
  .card .details{position:absolute;left:5px;bottom:5px;font-size:2.6px;line-height:1.35;color:var(--ink)}
  .card--dark .details{color:var(--grey-light)}
  .card .details strong{font-size:3.4px;color:var(--red)}

  /* letterhead */
  .letterhead{width:230px;height:259px;top:29px}
  .letterhead .brand{position:absolute;left:18px;top:12px;font-size:10px;font-weight:700;color:var(--red)}
  .letterhead .footer{position:absolute;left:0;right:0;bottom:6px;text-align:center;font-size:3.5px;color:var(--grey)}
  .letterhead .mark{position:absolute;left:0;right:0;top:108px;text-align:center;font-size:22px;font-weight:700;color:#ececec;line-height:1.1}

  /* envelope front */
  .envelope{width:209px;height:96px;left:691px}
  .envelope .brand{position:absolute;left:12px;top:10px;font-size:8px;font-weight:700;color:var(--red)}
  .envelope .return{position:absolute;left:12px;top:22px;font-size:3px;line-height:1.4;color:var(--grey)}

  /* envelope backs */
  .envelope-backs{position:absolute;left:936px;top:43px;width:245px;height:242px}
  .envelope-backs .url{font-family:"Montserrat",Arial,sans-serif;font-size:5px;fill:#ffffff;letter-spacing:.5px}
  .envelope-backs .url--dark{fill:var(--grey)}
</style>
</head>
<body>
<main class="canvas">

  <!-- business cards -->
  <section class="piece card" style="left:24px;top:115px">
    <svg class="trim" viewBox="0 0 79 43" preserveAspectRatio="none"><path d="M0 38 Q40 32 79 36 V43 H0Z" fill="var(--red)"/></svg>
    <p class="brand">KTL &amp; Associates</p>
  </section>
  <section class="piece card" style="left:108px;top:115px">
    <svg class="trim" viewBox="0 0 79 43" preserveAspectRatio="none"><path d="M0 0 H79 V4 Q40 8 0 3Z" fill="var(--red)"/></svg>
    <p class="brand" style="top:8px">KTL &amp; Associates</p>
    <div class="details"><strong>Gregory P. Holt</strong><br>Principal<br>2947 Brambleton Way Suite 340<br>Frisco, Texas 75981<br>gregory@ktlva.com · www.ktlva.com</div>
  </section>
  <section class="piece card card--dark" style="left:24px;top:173px">
    <p class="brand">KTL &amp; Associates</p>
    <p class="slogan">Passion. Performance. Results.</p>
  </section>
  <section class="piece card card--dark" style="left:108px;top:173px">
    <svg class="trim" viewBox="0 0 79 43" preserveAspectRatio="none"><path d="M0 39 Q40 35 79 38 V43 H0Z" fill="var(--red)"/></svg>
    <p class="brand" style="left:5px;top:7px;text-align:left">KTL &amp; Associates</p>
    <div class="details"><strong>Gregory P. Holt</strong><br>Principal<br>gregory@ktlva.com<br>www.ktlva.com</div>
  </section>

  <!-- letterheads -->
  <section class="piece letterhead" style="left:197px">
    <svg class="trim" viewBox="0 0 230 259" preserveAspectRatio="none">
      <path d="M0 0 H230 V8 Q120 22 0 10Z" fill="var(--red)"/>
      <path d="M0 10 Q120 22 230 8 V10 Q120 25 0 12Z" fill="var(--red-dark)"/>
      <path d="M0 244 Q110 236 230 246 V259 H0Z" fill="var(--red)"/>
      <path d="M0 242 Q110 234 230 244 V246 Q110 237 0 244Z" fill="var(--grey)"/>
    </svg>
    <p class="brand" style="top:22px">KTL &amp; Associates</p>
    <p class="footer" style="bottom:18px;color:var(--grey)">2947 Brambleton Way Suite 340 · Frisco, Texas 75981 · www.ktlva.com</p>
  </section>
  <section class="piece letterhead" style="left:444px">
    <svg class="trim" viewBox="0 0 230 259" preserveAspectRatio="none">
      <path d="M0 0 H230 V8 Q120 22 0 10Z" fill="var(--red)"/>
      <path d="M0 10 Q120 22 230 8 V10 Q120 25 0 12Z" fill="var(--red-dark)"/>
      <path d="M0 244 Q110 236 230 246 V259 H0Z" fill="var(--red)"/>
      <path d="M0 242 Q110 234 230 244 V246 Q110 237 0 244Z" fill="var(--grey)"/>
    </svg>
    <p class="brand" style="top:22px">KTL &amp; Associates</p>
    <p class="mark">KTL<br>&amp; Associates</p>
    <p class="footer" style="bottom:18px">2947 Brambleton Way Suite 340 · Frisco, Texas 75981 · www.ktlva.com</p>
  </section>

  <!-- envelope fronts -->
  <section class="piece envelope" style="top:43px">
    <svg class="trim" viewBox="0 0 209 96" preserveAspectRatio="none">
      <path d="M0 0 H209 V6 Q110 14 0 5Z" fill="var(--red)"/>
      <path d="M0 86 Q100 80 209 88 V96 H0Z" fill="var(--red)"/>
    </svg>
    <p class="brand">KTL &amp; Associates</p>
    <p class="return">2947 Brambleton Way Suite 340<br>Frisco, Texas 75981</p>
  </section>
  <section class="piece envelope" style="top:158px">
    <svg class="trim" viewBox="0 0 209 96" preserveAspectRatio="none">
      <path d="M0 0 H209 V6 Q110 14 0 5Z" fill="var(--red)"/>
      <path d="M0 86 Q100 80 209 88 V96 H0Z" fill="var(--red)"/>
    </svg>
    <p class="brand">KTL &amp; Associates</p>
    <p class="return">2947 Brambleton Way Suite 340<br>Frisco, Texas 75981</p>
  </section>

  <!-- envelope backs -->
  <svg class="envelope-backs" viewBox="0 0 245 242">
    <defs>
      <linearGradient id="flapRed" x1="0" y1="0" x2="0" y2="1"><stop offset="0" stop-color="#e02a2f"/><stop offset="1" stop-color="#9c0e12"/></linearGradient>
      <linearGradient id="flapGrey" x1="0" y1="0" x2="0" y2="1"><stop offset="0" stop-color="#d4d4d4"/><stop offset="1" stop-color="#8a8a8a"/></linearGradient>
      <linearGradient id="flapWhite" x1="0" y1="0" x2="0" y2="1"><stop offset="0" stop-color="#ffffff"/><stop offset="1" stop-color="#dcdcdc"/></linearGradient>
    </defs>
    <!-- bottom envelope -->
    <rect x="0" y="140" width="245" height="100" fill="#f4f4f4"/>
    <path d="M0 140 H245 L122 200Z" fill="url(#flapWhite)"/>
    <text class="url url--dark" x="122.5" y="180" text-anchor="middle">www.ktlva.com</text>
    <!-- middle envelope -->
    <rect x="0" y="70" width="245" height="70" fill="#ececec"/>
    <path d="M0 70 H245 L122 125Z" fill="url(#flapGrey)"/>
    <text class="url" x="122.5" y="92" text-anchor="middle">www.ktlva.com</text>
    <!-- top envelope -->
    <rect x="0" y="0" width="245" height="70" fill="#f8f8f8"/>
    <path d="M0 0 H245 L122 55Z" fill="url(#flapRed)"/>
    <text class="url" x="122.5" y="20" text-anchor="middle">www.ktlva.com</text>
  </svg>

</main>
</body>
</html>
```